One page site for a home improvement construction company

Looking for a nice, SEO-friendly, single page site for a local handyman. Here's a good example of a similar site: https://pelvoritbuildersnv.com/

My handyman client has many photos of projects (included), so we'd like a nice photo gallery, along with the usual stuff: google map embed, nice contact form (use Elementor native), maybe a place for a few inspirational quotes.

Important: we don't want to use anything other than Elementor Pro and (maybe) a few free plugins to do your design.

Name of business is “Dorian Welkast Home Improvement”

Target Market(s)

Homeowners in upscale communities

Coding

Coded - Design and coding required

Number of Pages Required

1 page

Font styles to use
Serif
Sans Serif

Requirements
Must have
• Must be Built in Elementor. Needs a photo gallery (project portfolio) section with supplied photos.
Nice to have
• A place for an inspirational quote
Should not have
• The top photo should not be Dorian, it should be about the work.

```html
<!DOCTYPE html>
<html lang="en">
<head>
<meta charset="utf-8">
<title>Dorian Welkast Home Improvement</title>
<link rel="stylesheet" href="https://fonts.googleapis.com/css2?family=Lato:wght@400;700;900&family=Oswald:wght@400;500&display=swap">
<style>
:root{
  --blue:#1553a5;
  --orange:#ff5a0a;
  --ink:#222;
  --grey:#efefef;
  --footer:#252525;
  --footer-deep:#1b1b1b;
  --white:#fff;
}
*{box-sizing:border-box;margin:0;padding:0}
html,body{width:1200px;height:4211px;overflow:hidden}
body{position:relative;font-family:'Lato',sans-serif;color:var(--ink);background:var(--white)}
.abs{position:absolute}
.brand{font-family:'Oswald',sans-serif;font-weight:400;text-transform:uppercase;line-height:1.1}
.btn{position:absolute;background:var(--orange);color:var(--white);border-radius:30px;font-weight:700;text-transform:uppercase;display:flex;align-items:center;justify-content:center}
.photo{position:absolute}

/* header */
.site-header{left:0;top:0;width:1200px;height:111px;background:var(--white)}
.site-header .brand{left:74px;top:26px;font-size:29px;color:#2d2d2d}
.nav a{position:absolute;top:36px;height:41px;line-height:41px;font-size:14px;font-weight:700;color:#333;text-decoration:none;text-transform:uppercase}
.nav a.active{background:var(--orange);color:var(--white);border-radius:22px;width:95px;text-align:center}

/* hero */
.hero{left:0;top:111px;width:1200px;height:677px;background:linear-gradient(160deg,#4b6a3a 0%,#7a4a2c 35%,#9b4a26 60%,#5a3422 100%)}
.hero-title{left:0;top:296px;width:1200px;text-align:center;font-size:48px;font-weight:900;color:var(--white);line-height:1.05;text-transform:uppercase}
.dots{left:562px;top:620px;display:flex;gap:10px}
.dots i{width:10px;height:10px;border-radius:50%;background:var(--white)}
.dots i:first-child{background:#f39a2b}

/* quote */
.quote{left:60px;top:668px;width:1080px;height:236px}
.quote p{position:absolute;left:80px;right:80px;top:60px;text-align:center;color:var(--white);font-size:25px;line-height:1.45}
.quote .who{top:152px;font-size:17px;font-weight:700;text-transform:uppercase}

/* about */
.about-frame{left:74px;top:974px;width:379px;height:378px;background:var(--orange)}
.about-photo{left:93px;top:993px;width:379px;height:377px;background:linear-gradient(180deg,#3f5a33,#6b7a55 45%,#4a6482)}
.about h2{position:absolute;left:535px;top:976px;font-size:38px;font-weight:900;line-height:42px;text-transform:uppercase;color:#222}
.about p{position:absolute;left:535px;top:1095px;width:565px;font-size:16.5px;line-height:30.5px;color:#444}

/* services */
.services-bg{left:0;top:1452px;width:1200px;height:306px}
.section-title{position:absolute;left:0;width:1200px;text-align:center;font-size:39px;font-weight:900;text-transform:uppercase;color:#333}
.services-sub{left:0;top:1578px;width:1200px;text-align:center;font-size:15px;color:#333}
.card{position:absolute;top:1633px;width:330px;height:290px;background:var(--blue);border-radius:6px}
.card .pic{position:absolute;left:13px;top:13px;width:304px;height:196px}
.card h3{position:absolute;left:0;top:224px;width:100%;text-align:center;color:var(--white);font-size:23px;font-weight:900;line-height:25px;text-transform:uppercase}

/* gallery */
.g{position:absolute;border-radius:6px}

/* contact */
.contact{left:60px;top:2986px;width:1080px;height:523px}
.field{position:absolute;background:var(--white);border-radius:24px;font-size:15.5px;color:#333;padding-left:25px;display:flex;align-items:center}
.field.msg{align-items:flex-start;padding-top:16px;border-radius:14px}

/* map */
.map{left:0;top:3509px;width:1200px;height:340px;background:linear-gradient(135deg,#e6eee0,#eef0ea 40%,#dfe8d8 70%,#e9ede4)}
.info-card{left:77px;top:3559px;width:327px;height:238px;background:var(--white);border-radius:10px;box-shadow:0 2px 10px rgba(0,0,0,.15);text-align:center}
.info-card h4{margin-top:32px;font-size:25px;font-weight:900;text-transform:uppercase;color:#333}
.info-card .co{margin-top:8px;font-size:16px;font-weight:900;line-height:26px;color:var(--orange);text-transform:uppercase}
.info-card .ln{font-size:13px;line-height:21px;color:#222}

/* footer */
.footer{left:0;top:3849px;width:1200px;height:296px;background:var(--footer)}
.footer-bar{left:0;top:4145px;width:1200px;height:66px;background:var(--footer-deep)}
.footer .brand{position:absolute;left:74px;top:82px;font-size:26px;color:#cfcfcf}
.footer .blurb{position:absolute;left:74px;top:156px;width:250px;font-size:13px;line-height:26px;color:#bbb}
.fhead{position:absolute;top:54px;font-size:16px;font-weight:700;color:var(--white);text-transform:uppercase}
.flinks{position:absolute;font-size:13.5px;line-height:31.5px;color:#ccc}
.fin{position:absolute;left:883px;width:244px;height:39px;background:#f3f3f3;border-radius:20px;font-size:13.5px;color:#444;padding-left:18px;display:flex;align-items:center}
.copy{left:74px;top:4178px;font-size:11.5px;color:#ddd}
.social{left:965px;top:4170px;display:flex;gap:18px}
.social i{width:16px;height:16px;border-radius:50%;background:#eee}
</style>
</head>
<body>

<header class="site-header abs">
  <div class="brand abs">Dorian Welkast Home<br>Improvement</div>
  <nav class="nav">
    <a class="active" style="left:407px">Home</a>
    <a style="left:517px">About Us</a>
    <a style="left:631px">Service</a>
    <a style="left:732px">Gallery</a>
    <a style="left:837px">Blog</a>
    <a style="left:917px">Reviews</a>
    <a style="left:1023px">Contact Us</a>
  </nav>
</header>

<div class="hero abs" role="img" aria-label="Photo of a finished redwood deck with a wooden pergola beside a house"></div>
<h1 class="hero-title abs">Dorian Welkast Home<br>Improvement</h1>
<div class="btn" style="left:505px;top:437px;width:188px;height:43px;font-size:16px">Contact Us</div>
<div class="dots abs"><i></i><i></i><i></i><i></i></div>

<section class="quote abs">
  <svg width="1080" height="236" viewBox="0 0 1080 236" style="position:absolute;left:0;top:0">
    <path d="M0,46 Q0,26 22,24 Q540,-8 1058,24 Q1080,26 1080,46 L1080,186 Q1080,204 1058,206 Q540,250 22,206 Q0,204 0,186 Z" fill="var(--blue)"/>
  </svg>
  <p>“ Etiam vel porttitor magna, sed rutrum lectus vivamus porta metus vel neque tempor fringilla. Vestibulum ante ipsum primis in faucibus”</p>
  <p class="who">Name Heading</p>
</section>

<section class="about">
  <div class="about-frame abs"></div>
  <div class="about-photo photo" role="img" aria-label="Portrait photo of Dorian outdoors in a plaid shirt"></div>
  <h2>Welcom to<br>Dorian Welkast Home<br>Improvement</h2>
  <p>Lorem ipsum dolor sit amet, consectetur adipiscing elit.&nbsp; Aliquam felis elit, dignissim a ornare non, elementum in enim.&nbsp; Pellentesque mauris turpis, ornare sit amet nibh vel, porta suscipit felis. Praesent finibus tincidunt vehicula. Duis nec quam ultrices, egestas odio nec, imperdiet elit. Curabitur vitae tincidunt mi, in eleifend diam. Aenean ut feugiat diam, quis molestie velit.&nbsp; Nam sit amet sagittis felis.</p>
  <div class="btn" style="left:535px;top:1313px;width:188px;height:46px;font-size:16px">Read More</div>
</section>

<svg class="services-bg abs" width="1200" height="306" viewBox="0 0 1200 306">
  <path d="M0,26 Q600,-26 1200,26 L1200,306 L0,306 Z" fill="var(--grey)"/>
</svg>
<h2 class="section-title" style="top:1505px">Our Services</h2>
<p class="services-sub abs">Lorem ipsum dolor sit amet, consectetur adipiscing elitliquam felis elit, dignissim a ornare non, elementum in enim.</p>
<div class="card" style="left:74px"><div class="pic" role="img" aria-label="Photo of an above-ground swimming pool with a wooden deck" style="background:linear-gradient(180deg,#6b5a45,#2f8ad8 40%,#1e78d0)"></div><h3>Donec tincidunt<br>efficitur</h3></div>
<div class="card" style="left:435px"><div class="pic" role="img" aria-label="Photo of a curved stone retaining wall in a yard" style="background:linear-gradient(180deg,#4e5d40,#8a8270 50%,#6e6656)"></div><h3>Donec tincidunt<br>efficitur</h3></div>
<div class="card" style="left:795px"><div class="pic" role="img" aria-label="Photo of a wooden pergola on a patio" style="background:linear-gradient(180deg,#7a5a3c,#8d6748 50%,#5d4a36)"></div><h3>Donec tincidunt<br>efficitur</h3></div>

<h2 class="section-title" style="top:2000px">Gallery</h2>
<div class="g" role="img" aria-label="Photo of a large timber pergola beside a house" style="left:74px;top:2088px;width:681px;height:404px;background:linear-gradient(180deg,#b9703f,#c48a5e 40%,#7d8d6e)"></div>
<div class="g" role="img" aria-label="Photo of a freshly stained red deck" style="left:770px;top:2088px;width:357px;height:198px;background:linear-gradient(180deg,#6a6050,#a3422e 45%,#8a3626)"></div>
<div class="g" role="img" aria-label="Photo of an old weathered deck before repair" style="left:770px;top:2296px;width:357px;height:196px;background:linear-gradient(180deg,#5c5a4e,#3a3a36 55%,#4a4a40)"></div>
<div class="g" role="img" aria-label="Photo of new wooden deck framing with steps" style="left:74px;top:2505px;width:358px;height:196px;background:linear-gradient(180deg,#8a8e92,#c99a5e 45%,#a87a45)"></div>
<div class="g" role="img" aria-label="Photo of a wooden deck built around a travel trailer" style="left:74px;top:2711px;width:358px;height:196px;background:linear-gradient(180deg,#5a8fd0,#8a8a86 45%,#a5703e)"></div>
<div class="g" role="img" aria-label="Photo of a gravel slope with a wooden railing and hot tub" style="left:446px;top:2505px;width:681px;height:402px;background:linear-gradient(160deg,#4f6b3a,#7b756a 40%,#9a958a 70%,#6e4a32)"></div>

<section class="contact abs">
  <svg width="1080" height="523" viewBox="0 0 1080 523" style="position:absolute;left:0;top:0">
    <path d="M0,46 Q0,26 22,24 Q540,-8 1058,24 Q1080,26 1080,46 L1080,523 L0,523 Z" fill="var(--blue)"/>
  </svg>
  <h2 class="abs" style="left:0;top:58px;width:1080px;text-align:center;font-size:36px;font-weight:900;color:var(--white);text-transform:uppercase">Get in Touch</h2>
  <div class="field" style="left:104px;top:140px;width:421px;height:48px">Name</div>
  <div class="field" style="left:553px;top:140px;width:422px;height:48px">Email Address</div>
  <div class="field" style="left:104px;top:204px;width:421px;height:49px">Phone No</div>
  <div class="field" style="left:553px;top:204px;width:422px;height:49px">Subject</div>
  <div class="field msg" style="left:104px;top:269px;width:871px;height:113px">Message</div>
  <div class="btn" style="left:437px;top:411px;width:206px;height:53px;font-size:19px">Submit</div>
</section>

<div class="map abs" role="img" aria-label="Embedded street map showing the business location"></div>
<div class="info-card abs">
  <h4>Contact Info</h4>
  <div class="co">Dorian Welkast Home<br>Improvement</div>
  <div class="ln" style="margin-top:14px">14 Alder Court, Street Name<br>Brookvale City, USA</div>
  <div class="ln" style="margin-top:5px">
    <svg width="12" height="12" viewBox="0 0 24 24" style="vertical-align:-1px;margin-right:8px"><path d="M6.6 10.8a15.1 15.1 0 006.6 6.6l2.2-2.2c.3-.3.7-.4 1-.2 1.1.4 2.3.6 3.6.6.6 0 1 .4 1 1V20c0 .6-.4 1-1 1A17 17 0 013 4c0-.6.4-1 1-1h3.5c.6 0 1 .4 1 1 0 1.3.2 2.5.6 3.6.1.3 0 .7-.2 1z" fill="#222"/></svg>1-800-555-0147
  </div>
  <div class="ln">
    <svg width="13" height="10" viewBox="0 0 26 20" style="vertical-align:0;margin-right:6px"><path d="M0 0h26v20H0z" fill="#222"/><path d="M1 1l12 9 12-9" stroke="#fff" stroke-width="2" fill="none"/></svg>hello@welkasthome.com
  </div>
</div>

<footer class="footer abs">
  <div class="brand">Dorian Welkast Home<br>Improvement</div>
  <p class="blurb">Lorem ipsum dolor sit amet, consec etur adipiscing elitnam tincidunt orci nec orci luctus, quis tincidunt massa molestie.</p>
  <div class="fhead" style="left:373px">Site Map</div>
  <div class="flinks" style="left:373px;top:84px">Home<br>About Us<br>Service<br>Gallery</div>
  <div class="flinks" style="left:494px;top:84px">Blog<br>Reviews<br>Contact Us</div>
  <div class="fhead" style="left:644px">Services</div>
  <div class="flinks" style="left:644px;top:80px;line-height:26px">Lorem ipsum<br>Solor sit ametconsec<br>etur adipiscing<br>Elitnam tincidunt orci<br>Nec orci luctus<br>Quis tincidunt</div>
  <div class="fhead" style="left:883px">Email Sign Up</div>
  <div class="fin" style="top:86px">Enter Name</div>
  <div class="fin" style="top:137px">Enter Email Address</div>
  <div class="btn" style="left:883px;top:188px;width:108px;height:39px;font-size:13.5px">Sign Up</div>
</footer>
<div class="footer-bar abs"></div>
<p class="copy abs">Copyright © 2020. Company Name.&nbsp; All Right Reserved</p>
<div class="social abs"><i></i><i></i><i></i><i></i><i></i></div>

</body>
</html>
```